Market place for used airplanes/helicopters/parts

http://www.vingtorget.se needs a facelift.

# What is it
Classifieds for used airplanes/helicopters/parts/spare parts/aviation literature, for people in Scandinavia. The number of classifieds is ~120-200. They are mainly in Swedish, English, Norwegian.

It's not a glamorous or luxurious business, but more for people with a genuine interest in flying, technical things.

Similar to sites like this, but they have much more classifieds than my site
http://www.skyquarry.com/list/list.aspx?ETID=1&setype=1&catid=6
http://www.lindqvistflyg.com/planes.asp?meny=1&typ=single
https://www.propwashdeals.com/cat.php?mode=listing&main=

# What I want
Design only - no code. I want a modern, maybe a bit bootstrap like, clean, simple, not flashy, web design. I want the design to be in English.

# Audience of the website
Aviation interested men, 45-65 years old, in the nordic countries (around Sweden).

# Logotype that could be used (but not necessarily)
http://www.vingtorget.se/flygplan_till_salu_large.jpg
http://www.vingtorget.se/flygplan_till_salu.eps

Reason: I decided to extend the deadline with 1 day. The reason is that I (unfortunately) managed to put the contest in the wrong category for 1 day + I want to give you all feedback (been too busy the whole day, sorry).

Hi all! 

Thanks everyone for the contributions you made. 

I will setup a poll for the designs that I like most. Will get back when I have more information. 

Thanks and have a nice weekend!
Kjell

Target Market(s)

45-65 old Scandinavian men

Industry/Entity Type

Business

Requirements
Must have
• - A list with classifieds on the first page, so the visitor easily can see new classifieds.
- A classifieds should be able to have more than one photo
- A simple navigation for showing classifieds from categories like airplanes, helicopters/gyrocopters, parts, literature, misc (maybe other categories) .... but still, it's just 100-200 ads so it's not needed that much filtration.

- A placeholder/way of showing aviation news/clips. In the old design I had, it was a column to the right. It's enough to show maybe 2-5 placeholders.
- A placeholder for PlaceAds ads somewhere on the site.
Should not have
• - Carousels
- Too much clutter

```html
<!DOCTYPE html>
<html lang="en">
<head>
<meta charset="utf-8">
<title>Vingtorget – Aircraft Classifieds</title>
<link rel="stylesheet" href="https://fonts.googleapis.com/css2?family=Montserrat:wght@400;600;700&display=swap">
<style>
  :root {
    --bg: #efefef;
    --panel: #ffffff;
    --brand: #1f5fa8;
    --brand-dark: #17457c;
    --search-blue: #1778c2;
    --nav: #3b3b3b;
    --nav-divider: #2a2a2a;
    --text: #2b2b2b;
    --muted: #9a9a9a;
    --rule: #cfcfcf;
    --ad: #8c8c8c;
    --photo-sky: #8d97a6;
    --photo-ground: #6d6f72;
    --placeholder: #ececec;
  }
  * { box-sizing: border-box; margin: 0; padding: 0; }
  html, body { width: 1200px; height: 788px; overflow: hidden; }
  body {
    background: linear-gradient(180deg, #f6f6f6 0%, var(--bg) 100%);
    font-family: "Montserrat", Arial, sans-serif;
    color: var(--text);
    position: relative;
  }
  .page {
    position: absolute; left: 264px; top: 20px;
    width: 672px; height: 727px;
    background: var(--panel);
  }
  .brand {
    position: absolute; left: 15px; top: 26px;
    display: flex; align-items: center; gap: 7px;
    font-weight: 700; font-size: 20px; letter-spacing: .5px;
    color: var(--brand);
  }
  .brand-mark { width: 12px; height: 12px; border-radius: 50%; background: var(--brand); }
  .search {
    position: absolute; left: 506px; top: 32px;
    width: 152px; height: 21px;
    background: var(--search-blue);
    border: 1px solid var(--brand-dark);
    display: flex; align-items: center; padding: 2px;
  }
  .search-field { flex: 1; height: 15px; background: #fff; border: 1px solid #0f5c98; }
  .search-btn {
    width: 38px; text-align: center; color: #fff;
    font-size: 7px; font-weight: 700; letter-spacing: .3px;
  }
  .hero {
    position: absolute; left: 13px; top: 75px;
    width: 645px; height: 125px;
    background: linear-gradient(180deg, #c9c2d2 0%, #9aa6b6 45%, #6f7885 70%, #5f6166 100%);
  }
  .filters {
    position: absolute; left: 13px; top: 200px;
    width: 645px; height: 24px;
    background: var(--nav);
    display: flex; align-items: center;
    box-shadow: 0 2px 3px rgba(0,0,0,.25);
  }
  .filter {
    display: flex; align-items: center; gap: 5px;
    height: 100%; padding: 0 9px;
    border-right: 1px solid var(--nav-divider);
    color: #fff; font-size: 7.5px; font-weight: 700; letter-spacing: .2px;
  }
  .check {
    width: 9px; height: 9px; background: #fff; display: block;
  }
  .show {
    margin-left: auto; display: flex; align-items: center; gap: 4px;
    color: #fff; font-size: 7.5px; padding-right: 6px;
  }
  .select {
    width: 88px; height: 15px; background: #fff; border: 1px solid #bbb;
    color: #444; font-size: 7.5px; display: flex; align-items: center;
    padding-left: 5px; position: relative;
  }
  .select::after {
    content: ""; position: absolute; right: 0; top: 0; width: 14px; height: 13px;
    border-left: 1px solid #ccc;
    background: linear-gradient(#fafafa, #e6e6e6);
  }
  .view-toggle { display: flex; gap: 8px; margin-left: 14px; }
  .view-toggle svg { display: block; }

  .listings {
    position: absolute; left: 12px; top: 237px;
    width: 478px; height: 464px;
    border: 1px solid var(--rule);
    padding: 9px 9px 0 9px;
  }
  .ad-item {
    display: flex; height: 131px;
    border-bottom: 1px solid var(--rule);
    margin-bottom: 12px;
  }
  .ad-item:last-of-type { border-bottom: none; margin-bottom: 0; }
  .photo-main {
    width: 155px; height: 117px; flex: none;
    background: linear-gradient(180deg, var(--photo-sky) 0%, #9aa0a8 50%, var(--photo-ground) 62%, #7a7a7a 100%);
  }
  .thumbs { display: flex; flex-direction: column; gap: 4px; margin-left: 6px; flex: none; }
  .thumb {
    width: 49px; height: 36px;
    background: linear-gradient(180deg, var(--photo-sky) 0%, #9aa0a8 50%, var(--photo-ground) 62%, #7a7a7a 100%);
  }
  .placeholder .photo-main, .placeholder .thumb { background: var(--placeholder); }
  .ad-body { margin-left: 18px; width: 232px; }
  .ad-title { display: flex; align-items: baseline; gap: 6px; margin-top: -2px; }
  .ad-name { font-size: 15px; font-weight: 700; color: var(--brand); letter-spacing: .2px; }
  .ad-cat { font-size: 7px; font-weight: 600; color: var(--text); letter-spacing: .2px; }
  .ad-desc, .ad-contact { font-size: 8.4px; line-height: 10.6px; margin-top: 8px; }

  .pager {
    position: absolute; left: 0; right: 0; bottom: 18px;
    text-align: center; font-size: 7.5px;
  }
  .pager span { margin: 0 3px; }
  .pager .prev { color: #bbb; }
  .pager .current { color: var(--brand); font-weight: 700; }
  .pager .page-link { text-decoration: underline; }

  .ad-slot {
    position: absolute; left: 501px; width: 157px; height: 167px;
    background: var(--ad);
    display: flex; align-items: center; justify-content: center;
    color: #fff; font-weight: 700; font-size: 17px; letter-spacing: .5px;
  }
  .ad-slot.first { top: 237px; }
  .ad-slot.second { top: 415px; }

  .footer {
    position: absolute; left: 279px; top: 761px;
    font-size: 7.5px; color: #444;
  }
</style>
</head>
<body>
  <div class="page">
    <div class="brand"><span class="brand-mark"></span>VINGTORGET</div>

    <div class="search">
      <div class="search-field"></div>
      <div class="search-btn">SEARCH</div>
    </div>

    <div class="hero" role="img" aria-label="Photo of a blue and white high-wing light aircraft parked on an airfield apron"></div>

    <nav class="filters">
      <div class="filter">
        <svg class="check" viewBox="0 0 9 9"><rect width="9" height="9" fill="#fff"/><path d="M1.8 4.6l2 2 3.6-4.4" stroke="#1f5fa8" stroke-width="1.6" fill="none"/></svg>AIRPLANES
      </div>
      <div class="filter">
        <svg class="check" viewBox="0 0 9 9"><rect width="9" height="9" fill="#fff"/><path d="M1.8 4.6l2 2 3.6-4.4" stroke="#1f5fa8" stroke-width="1.6" fill="none"/></svg>HELICOPTERS
      </div>
      <div class="filter"><span class="check"></span>PARTS</div>
      <div class="filter"><span class="check"></span>SPARE PARTS</div>
      <div class="filter"><span class="check"></span>AVIATION LITERATURE</div>
      <div class="show">
        Show:
        <div class="select">200 ads</div>
        <div class="view-toggle">
          <svg width="12" height="12" viewBox="0 0 12 12"><rect x="0" y="0" width="5" height="5" fill="#999"/><rect x="7" y="0" width="5" height="5" fill="#999"/><rect x="0" y="7" width="5" height="5" fill="#999"/><rect x="7" y="7" width="5" height="5" fill="#999"/></svg>
          <svg width="15" height="15" viewBox="0 0 15 15"><rect width="15" height="15" fill="#eee"/><rect x="2" y="2" width="4" height="4" fill="#555"/><rect x="7" y="2" width="6" height="1.5" fill="#555"/><rect x="7" y="4.5" width="6" height="1.5" fill="#555"/><rect x="2" y="8" width="4" height="4" fill="#555"/><rect x="7" y="8" width="6" height="1.5" fill="#555"/><rect x="7" y="10.5" width="6" height="1.5" fill="#555"/></svg>
        </div>
      </div>
    </nav>

    <main class="listings">
      <article class="ad-item">
        <div class="photo-main" role="img" aria-label="Photo of a blue and white low-wing aircraft in front of a hangar"></div>
        <div class="thumbs">
          <div class="thumb" role="img" aria-label="Aircraft photo thumbnail"></div>
          <div class="thumb" role="img" aria-label="Aircraft photo thumbnail"></div>
          <div class="thumb" role="img" aria-label="Aircraft photo thumbnail"></div>
        </div>
        <div class="ad-body">
          <div class="ad-title"><span class="ad-name">VALK6</span><span class="ad-cat">AIRPLANES</span></div>
          <p class="ad-desc">Vi sonderar marknaden för vår UL klassade Valk, bygd 1997. Maskinen är i mycket gott skick. 1120tim totalt, 430tim på motor &amp; prop. Flottörfästen installerade. 350.000:-<br>Låter det intressant? skicka ett mail.</p>
          <p class="ad-contact">Gunnar<br>Namn: Gunnar Lindahl, E-posta<br>Telefon: 070-5551842<br>Datum: 2013-09-27 06:55:21</p>
        </div>
      </article>

      <article class="ad-item placeholder">
        <div class="photo-main" role="img" aria-label="Empty photo placeholder"></div>
        <div class="thumbs">
          <div class="thumb" role="img" aria-label="Empty thumbnail placeholder"></div>
          <div class="thumb" role="img" aria-label="Empty thumbnail placeholder"></div>
          <div class="thumb" role="img" aria-label="Empty thumbnail placeholder"></div>
        </div>
        <div class="ad-body">
          <div class="ad-title"><span class="ad-name">VALK6</span><span class="ad-cat">AIRPLANES</span></div>
          <p class="ad-desc">Vi sonderar marknaden för vår UL klassade Valk, bygd 1997. Maskinen är i mycket gott skick. 1120tim totalt, 430tim på motor &amp; prop. Flottörfästen installerade. 350.000:-<br>Låter det intressant? skicka ett mail.</p>
          <p class="ad-contact">Gunnar<br>Namn: Gunnar Lindahl, E-posta<br>Telefon: 070-5551842<br>Datum: 2013-09-27 06:55:21</p>
        </div>
      </article>

      <article class="ad-item">
        <div class="photo-main" role="img" aria-label="Photo of a blue and white low-wing aircraft in front of a hangar"></div>
        <div class="thumbs">
          <div class="thumb" role="img" aria-label="Aircraft photo thumbnail"></div>
          <div class="thumb" role="img" aria-label="Aircraft photo thumbnail"></div>
          <div class="thumb" role="img" aria-label="Aircraft photo thumbnail"></div>
        </div>
        <div class="ad-body">
          <div class="ad-title"><span class="ad-name">VALK6</span><span class="ad-cat">AIRPLANES</span></div>
          <p class="ad-desc">Vi sonderar marknaden för vår UL klassade Valk, bygd 1997. Maskinen är i mycket gott skick. 1120tim totalt, 430tim på motor &amp; prop. Flottörfästen installerade. 350.000:-<br>Låter det intressant? skicka ett mail.</p>
          <p class="ad-contact">Gunnar<br>Namn: Gunnar Lindahl, E-posta<br>Telefon: 070-5551842<br>Datum: 2013-09-27 06:55:21</p>
        </div>
      </article>

      <div class="pager">
        <span class="prev">« Previous</span><span class="current">1</span><span class="page-link">2</span><span>Next »</span>
      </div>
    </main>

    <aside class="ad-slot first">PLACEADS</aside>
    <aside class="ad-slot second">PLACEADS</aside>
  </div>

  <footer class="footer">© 2013 VINGTORGET</footer>
</body>
</html>
```